VaultMeridan Business Card Re-Design

VaultMeridan is a specialized information security company that applies its proven methodology of security Assessment, Development, Integration and Training (A-D-I-T) to provide cyber security services in the areas of Data Protection, Network Defense and Compliance. We need the current business card re-designed to properly scale the fonts and possibly rearranging some elements (icons, lettering, etc.) to make the card more appealing to the eye. The card should have the logo that is on the web site (www.vaultmeridan-example.com). We would like ideas for both a black card (black background) and a white card (white background). We prefer rounded corners to help the card stand out but are open to all ideas. FYI: VaultMeridan's slogan is "...your security is our business".

Target Market(s)

#1 US Government Contracting Companies, #2 Commercial Companies, #3 Gen. Public.

Industry/Entity Type

Business

Contact Information for Business Card

See Description; open to the use of different fonts.

Font styles to use
Sans Serif

Colors
000000
ec1f27
ffffff

Requirements
Must have
• Company logo on web site, rounded corners, list of company offerings on the back of the card.
Nice to have
• Icons
Should not have
• none

```html
<!DOCTYPE html>
<html lang="en">
<head>
<meta charset="utf-8">
<title>VaultMeridan Business Card</title>
<link rel="stylesheet" href="https://fonts.googleapis.com/css2?family=Arimo:wght@400;700&display=swap">
<style>
  :root {
    --ink: #000000;
    --red: #ec1f27;
    --red-soft: #d8433b;
    --red-fold: #b8312b;
    --paper: #ffffff;
    --stage: #eeeeee;
    --text: #111111;
  }
  * { box-sizing: border-box; margin: 0; padding: 0; }
  html, body { width: 1200px; height: 675px; overflow: hidden; }
  body {
    background: var(--stage);
    font-family: "Arimo", Arial, sans-serif;
    color: var(--text);
    position: relative;
  }
  .card {
    position: absolute;
    top: 160px;
    width: 540px;
    height: 355px;
    background: var(--paper);
    border-radius: 10px;
    overflow: hidden;
    box-shadow: 0 6px 22px rgba(0,0,0,0.18);
  }
  .card--front { left: 40px; }
  .card--back { left: 620px; }

  /* Front */
  .brand {
    position: absolute;
    left: 0; top: 110px;
    width: 284px;
    text-align: center;
  }
  .brand__name {
    display: inline-flex;
    align-items: center;
    gap: 10px;
    font-size: 30px;
    font-weight: 400;
    letter-spacing: 1px;
    color: var(--ink);
    white-space: nowrap;
  }
  .brand__square { width: 14px; height: 14px; background: var(--red); }
  .brand__tagline {
    margin-top: 18px;
    font-size: 10.5px;
    font-weight: 700;
    letter-spacing: 0.4px;
  }
  .name-band {
    position: absolute;
    left: 284px; top: 67px;
    width: 256px; height: 53px;
    background: var(--ink);
    color: var(--paper);
    padding: 7px 0 0 38px;
    white-space: nowrap;
  }
  .name-band__name { font-size: 23px; }
  .name-band__creds { font-size: 9px; margin-left: 4px; }
  .name-band__title { font-size: 11px; margin-top: 2px; }
  .contact-panel { position: absolute; left: 284px; top: 120px; }
  .contact-list {
    position: absolute;
    left: 334px; top: 145px;
    list-style: none;
  }
  .contact-list li {
    display: flex;
    align-items: center;
    height: 28px;
    font-size: 11px;
    white-space: nowrap;
  }
  .contact-list svg { width: 16px; height: 15px; margin-right: 10px; flex: none; }
  .address-band {
    position: absolute;
    left: 0; bottom: 0;
    width: 100%; height: 45px;
    background: var(--ink);
    color: var(--paper);
    font-size: 10.5px;
    display: flex;
    align-items: center;
    justify-content: center;
    gap: 10px;
    white-space: nowrap;
  }

  /* Back */
  .back-brand {
    position: absolute;
    top: 58px; left: 0; width: 100%;
    text-align: center;
  }
  .services {
    position: absolute;
    top: 160px;
    list-style: none;
    font-size: 9.5px;
    line-height: 17.6px;
    white-space: nowrap;
  }
  .services--left { left: 56px; }
  .services--right { left: 292px; }
  .slogan-band {
    position: absolute;
    left: 0; bottom: 0;
    width: 100%; height: 45px;
    background: var(--ink);
    color: var(--paper);
    font-size: 15px;
    display: flex;
    align-items: center;
    justify-content: center;
  }
</style>
</head>
<body>

<section class="card card--front" aria-label="Card front">
  <div class="brand">
    <div class="brand__name"><span class="brand__square"></span>VaultMeridan</div>
    <div class="brand__tagline">Information Security Solutions</div>
  </div>

  <div class="name-band">
    <div><span class="name-band__name">Marcus Hale</span><span class="name-band__creds">CISSP, C|EH</span></div>
    <div class="name-band__title">President - CEO</div>
  </div>

  <svg class="contact-panel" width="256" height="190" viewBox="0 0 256 190">
    <rect x="0" y="0" width="256" height="190" fill="var(--red-soft)"/>
    <polygon points="0,0 40,20 40,170 0,190" fill="var(--red-fold)"/>
    <rect x="40" y="20" width="216" height="150" fill="var(--paper)"/>
  </svg>

  <ul class="contact-list">
    <li>
      <svg viewBox="0 0 18 16"><rect x="5" y="1" width="8" height="14" rx="1.5" fill="var(--red)"/><rect x="6.5" y="3" width="5" height="7" fill="var(--paper)"/></svg>
      555.014.2287
    </li>
    <li>
      <svg viewBox="0 0 18 16"><path d="M2 6 Q9 0 16 6 L14 8 L12 6 L6 6 L4 8 Z" fill="none" stroke="var(--red)" stroke-width="1.3"/><rect x="4" y="8" width="10" height="6" rx="1" fill="none" stroke="var(--red)" stroke-width="1.3"/></svg>
      555.019.4410
    </li>
    <li>
      <svg viewBox="0 0 18 16"><circle cx="9" cy="8" r="6.5" fill="none" stroke="var(--red)" stroke-width="1.3"/><ellipse cx="9" cy="8" rx="2.8" ry="6.5" fill="none" stroke="var(--red)" stroke-width="1"/><line x1="2.5" y1="8" x2="15.5" y2="8" stroke="var(--red)" stroke-width="1"/></svg>
      www.vaultmeridan-example.com
    </li>
    <li>
      <svg viewBox="0 0 18 16"><rect x="1" y="3" width="16" height="11" fill="var(--red)"/><polyline points="1,3 9,10 17,3" fill="none" stroke="var(--paper)" stroke-width="1.4"/></svg>
      info@vaultmeridan-example.com
    </li>
    <li>
      <svg viewBox="0 0 18 16"><rect x="1" y="3" width="16" height="11" fill="var(--red)"/><polyline points="1,3 9,10 17,3" fill="none" stroke="var(--paper)" stroke-width="1.4"/></svg>
      mhale@vaultmeridan-example.com
    </li>
  </ul>

  <div class="address-band">
    <svg width="12" height="16" viewBox="0 0 12 16"><path d="M6 1 C2.5 1 1 3.5 1 6 C1 9 6 15 6 15 C6 15 11 9 11 6 C11 3.5 9.5 1 6 1 Z" fill="none" stroke="var(--paper)" stroke-width="1.4"/><circle cx="6" cy="6" r="1.8" fill="var(--paper)"/></svg>
    <span>VaultMeridan, Inc. // 1420 Harbor Point Dr. Suite 210 // Easton, Maryland 21601</span>
  </div>
</section>

<section class="card card--back" aria-label="Card back">
  <div class="back-brand">
    <div class="brand__name"><span class="brand__square"></span>VaultMeridan</div>
  </div>

  <ul class="services services--left">
    <li>Secure Cloud &amp; Open Stock Solutions</li>
    <li>Network Attack Penetration &amp; Defense</li>
    <li>Red/Blue Team</li>
    <li>Data Center Consolidation</li>
    <li>Secure Virtual Computing</li>
    <li>Classified Cross Domain Solutions</li>
    <li>Foreign/Counter Intelligence Data Security</li>
  </ul>
  <ul class="services services--right">
    <li>Certification and Accreditation</li>
    <li>Secure Wireless Solutions</li>
    <li>Security Training, Assessment &amp; Integration</li>
    <li>Security Subject Matter Experts</li>
    <li>Executive Security Strategy Coaching</li>
    <li>Data Encryption/Privacy</li>
  </ul>

  <div class="slogan-band">“Your security is our business.”</div>
</section>

</body>
</html>
```